Design 5 colour schemes for one web page

We are looking for 5 different colour schemes for our product template to create different kinds of colour tone for our web page, it doesn't need to be restructure the layout, just need to provide different color solution.

Please refer to the attached images and take note of the following when you’re working on the design:
(1) Please precisely reproduce the layout. Cannot remove or delete any wordings, components or column shown in the images.
(2) Okay to revise icons, background color or text style as you prefer. But cannot move/delete them.
(3) Provide PSD source files with good layer management. HTML/CSS are not required.
(4) Make reasonable and professional design.

After completion, please send back:
(1) 5 images with 5 different colour schemes.
(2) Related PSD files.

Industry/Entity Type

Management

Number of Pages Required

1 page

Font styles to use
Serif
Sans Serif

Requirements
Must have
• (1) 5 images for the colour schemes.
• (2) 5 PSD source files with good layer management.
Nice to have
• (1) Explanation about your design of the colour schemes.
Should not have
• (1) HTML/CSS code are not required.

```html
<!DOCTYPE html>
<html lang="en">
<head>
<meta charset="utf-8">
<title>Sports – Today</title>
<link href="https://fonts.googleapis.com/css2?family=Lato:wght@300;400;700;900&display=swap" rel="stylesheet">
<style>
:root{
  --orange:#ff8400;
  --orange-deep:#f27a00;
  --orange-league:#e87800;
  --brown:#8b3a1f;
  --dark:#333333;
  --dark-tab:#444444;
  --bar:#555555;
  --cream:#fef6cf;
  --blue:#1a8fe0;
  --red:#e0000e;
  --ink:#333333;
  --line:#e4e4e4;
  --white:#ffffff;
}
*{box-sizing:border-box;margin:0;padding:0}
html,body{width:1200px;height:1200px;overflow:hidden;background:var(--white)}
body{font-family:'Lato',sans-serif;color:var(--ink)}
.viewport{width:1200px;height:1200px;overflow:hidden;position:relative}
.page{width:1400px;height:1400px;position:absolute;left:0;top:0;transform:scale(.857143);transform-origin:0 0;background:#fff}
.abs{position:absolute}

.topbar{left:0;top:0;width:1400px;height:53px;background:var(--dark);color:#fff;font-size:12px;font-weight:700}
.topnav{position:absolute;left:201px;top:17px;display:flex;gap:30px;align-items:center}
.badge{background:#e0452a;border-radius:4px;padding:5px 7px;margin-left:-8px;font-size:11px}
.greet{position:absolute;left:823px;top:17px}
.wallet{position:absolute;left:917px;top:11px;width:190px;height:27px;background:#1e1e1e;border-radius:4px;display:flex;align-items:center;padding:0 12px;justify-content:space-between}
.signout{position:absolute;left:1113px;top:11px;width:87px;height:27px;background:#1e1e1e;border-radius:4px;display:flex;align-items:center;justify-content:center}

.masthead{left:0;top:53px;width:1400px;height:106px;background:var(--orange)}
.brand{position:absolute;left:198px;top:16px;color:#fff;font-size:58px;font-weight:300;letter-spacing:1px}
.tab-sports{position:absolute;left:463px;top:52px;width:117px;height:54px;background:var(--dark-tab);border-radius:4px 4px 0 0;color:#fff;font-weight:700;font-size:15px;display:flex;align-items:center;justify-content:center}
.results{position:absolute;left:1093px;top:9px;width:107px;height:28px;background:#ff9a2e;border-radius:3px;color:#fff;font-weight:900;font-size:14px;display:flex;align-items:center;justify-content:center;gap:8px;text-decoration:underline}

.toolbar{left:0;top:159px;width:1400px;height:41px;background:var(--bar);color:#eee;font-size:13px}
.lang{position:absolute;left:201px;top:12px;display:flex;gap:7px;align-items:center}
.clock{position:absolute;left:351px;top:13px;font-size:12px;letter-spacing:.3px}
.toolsep{position:absolute;top:4px;width:1px;height:33px;background:#6a6a6a}
.tool{position:absolute;top:14px;font-size:10px;color:#ddd}

.side{left:200px;width:184px}
.side-head{height:44px;background:var(--orange);color:#fff;font-weight:700;font-size:14px;display:flex;align-items:center;justify-content:center}
.fav-body{height:76px;background:var(--cream);padding:15px 14px}
.fav-hint{border:1px dashed #c9a64a;padding:6px 4px;font-size:11.5px;line-height:14px;color:#6b5a2a;text-align:center}
.sports-panel{top:345px;height:660px;background:var(--orange);border-radius:3px}
.tabs{display:flex;height:38px}
.tabs div{flex:1;display:flex;align-items:center;justify-content:center;color:#fff;font-weight:700;font-size:14px}
.tabs .off{background:var(--dark-tab)}
.sport-list{list-style:none;padding:6px 12px 0 14px}
.sport-list li{height:30px;border-bottom:1px solid rgba(255,255,255,.35);display:flex;align-items:center;color:#fff;font-size:12px;font-weight:700}
.sport-list li:last-child{border-bottom:none}
.sport-list .ico{width:14px;height:14px;border:2px solid #fff;border-radius:50%;margin-right:7px}
.sport-list .n{margin-left:auto}
.ticket{top:1018px;height:52px;display:flex;background:var(--orange)}
.ticket div{display:flex;align-items:center;justify-content:center;color:#fff;font-weight:700;font-size:14px}
.ticket .t1{width:99px}
.ticket .t2{flex:1;background:var(--dark-tab);height:38px;gap:5px}
.cnt{background:#111;border-radius:3px;padding:1px 5px;font-size:12px}
.mybets-body{height:122px;background:var(--cream);text-align:center;padding-top:12px;font-size:14px}
.nopend{margin:10px 11px 0;height:29px;background:#4c4c4c;border-radius:3px;color:#fff;font-weight:700;display:flex;align-items:center;justify-content:center}
.viewall{margin-top:15px;font-weight:700;font-size:14px}

.board{left:391px;width:809px;box-shadow:0 1px 3px rgba(0,0,0,.15)}
.board-head{height:43px;background:var(--orange);color:#fff;font-weight:700;font-size:14px;position:relative;border-radius:3px 3px 0 0}
.board-head .title{position:absolute;left:10px;top:13px;display:flex;gap:6px;align-items:center}
.board-head .count{position:absolute;left:389px;top:14px;display:flex;gap:4px;align-items:center}
.board-head .pick{position:absolute;right:8px;top:13px;display:flex;gap:5px;align-items:center}
.cols,.match{display:grid;grid-template-columns:64px 181px 44px 75px 105px 50px 76px 104px 52px 58px}
.colhead{height:38px;background:var(--orange-deep);color:#fff;font-size:12px;font-weight:700;grid-template-rows:18px 20px}
.colhead .cell{border-right:1px solid rgba(255,255,255,.5);display:flex;align-items:center;justify-content:center}
.h-time{grid-column:1;grid-row:1/3}
.h-event{grid-column:2;grid-row:1/3}
.h-full{grid-column:3/7;grid-row:1;border-bottom:1px solid rgba(255,255,255,.5)}
.h-half{grid-column:7/10;grid-row:1;border-bottom:1px solid rgba(255,255,255,.5)}
.h-more{grid-column:10;grid-row:1/3;border-right:none!important}
.colhead .sub{grid-row:2}
.league{height:28px;color:#fff;font-size:12px;font-weight:700;display:flex;align-items:center;padding-left:70px;position:relative}
.league.live{background:var(--brown)}
.league.pre{background:var(--orange-league)}
.league .st{margin-right:6px;font-size:13px;color:#ddd}
.league .rf{position:absolute;right:21px;top:7px}
.match{height:54px;border-bottom:1px solid var(--line);font-size:12px;font-weight:700;background:#fff}
.match.one{height:38px}
.match>div{border-right:1px solid var(--line);position:relative}
.match>div:last-child{border-right:none}
.c-time{padding:5px 0 0 29px;line-height:14px}
.c-time .chart{position:absolute;left:6px;top:13px;width:14px;height:13px;background:#555;border-radius:2px}
.c-time .chart::after{content:"";position:absolute;left:3px;bottom:3px;width:8px;height:5px;border-left:2px solid #fff;border-right:2px solid #fff}
.c-time i{display:block;color:var(--red);padding-left:9px}
.c-event{padding:5px 0 0 25px;line-height:14.5px}
.c-event .fav{position:absolute;left:6px;top:17px;color:#999;font-weight:400}
.away{color:var(--red)}
.l1{position:absolute;top:5px}
.l2{position:absolute;top:19px}
.blue{color:var(--blue)}
.red{color:var(--red)}
.ou-o{font-weight:400;color:#555}
.c-more{display:flex;align-items:center;justify-content:center;gap:3px}

.foot{left:471px;top:1326px;display:flex;gap:18px;font-size:14px;color:#666}
</style>
</head>
<body>
<div class="viewport">
<div class="page">

  <div class="abs topbar">
    <nav class="topnav"><span>MY BETS</span><span>STATEMENT</span><span>PREFERENCE</span><span>ANNOUNCEMENTS</span><span class="badge">99+</span></nav>
    <span class="greet">HI, STWTG036</span>
    <div class="wallet"><span>›› SD$</span><span>10,072.00 ↻</span></div>
    <div class="signout">SIGN OUT</div>
  </div>

  <header class="abs masthead">
    <div class="brand">LOGO</div>
    <div class="tab-sports">SPORTS</div>
    <div class="results">
      <svg width="16" height="14" viewBox="0 0 16 14"><path d="M3 1h10v4a5 5 0 0 1-10 0z M1 2h2v3H2z M13 2h2l-1 3h-1z M7 10h2v2h2v2H5v-2h2z" fill="#fff"/></svg>
      <span>RESULTS</span>
    </div>
  </header>

  <div class="abs toolbar">
    <div class="lang"><svg width="16" height="16"><circle cx="8" cy="8" r="7" fill="none" stroke="#ccc" stroke-width="2"/></svg>English (Asia)</div>
    <span class="toolsep" style="left:333px"></span>
    <div class="clock">12/02/2013 15:53PM GMT+8</div>
    <span class="tool" style="left:874px">⊞ ▾</span>
    <span class="toolsep" style="left:914px"></span>
    <span class="tool" style="left:928px">★ ▾</span>
    <span class="toolsep" style="left:965px"></span>
    <span class="tool" style="left:980px">☰ ▾</span>
    <span class="toolsep" style="left:1020px"></span>
    <span class="tool" style="left:1035px">MY ▾</span>
    <span class="toolsep" style="left:1075px"></span>
    <span class="tool" style="left:1089px">◀)</span>
    <span class="toolsep" style="left:1115px"></span>
    <span class="tool" style="left:1130px">▣</span>
    <span class="toolsep" style="left:1157px"></span>
    <span class="tool" style="left:1171px">Live</span>
  </div>

  <section class="abs side" style="top:213px">
    <div class="side-head">My Favourites</div>
    <div class="fav-body"><div class="fav-hint">Click o an event or league to add it to "My Favourites"</div></div>
  </section>

  <section class="abs side sports-panel">
    <div class="tabs"><div>Sports</div><div class="off">Markets</div></div>
    <ul class="sport-list">
      <li><span class="ico"></span>Football<span class="n">600</span></li>
      <li><span class="ico"></span>Basketball<span class="n">600</span></li>
      <li><span class="ico"></span>Baseball<span class="n">600</span></li>
      <li><span class="ico"></span>Tennis<span class="n">600</span></li>
      <li><span class="ico"></span>American Football<span class="n">600</span></li>
      <li><span class="ico"></span>Badminton<span class="n">600</span></li>
      <li><span class="ico"></span>Boxing<span class="n">600</span></li>
      <li><span class="ico"></span>Cricket<span class="n">600</span></li>
      <li><span class="ico"></span>Cycling<span class="n">600</span></li>
      <li><span class="ico"></span>Darts<span class="n">600</span></li>
      <li><span class="ico"></span>Entertainment<span class="n">600</span></li>
      <li><span class="ico"></span>Golf<span class="n">600</span></li>
      <li><span class="ico"></span>Handball<span class="n">600</span></li>
      <li><span class="ico"></span>Ice Hockey<span class="n">600</span></li>
      <li><span class="ico"></span>Mixed Martial Arts<span class="n">600</span></li>
      <li><span class="ico"></span>Motor Sport<span class="n">600</span></li>
      <li><span class="ico"></span>Pool/Snooker<span class="n">600</span></li>
      <li><span class="ico"></span>Rugby<span class="n">600</span></li>
      <li><span class="ico"></span>Volleyball<span class="n">600</span></li>
      <li><span class="ico"></span>Winter Sports<span class="n">600</span></li>
    </ul>
  </section>

  <section class="abs side ticket"><div class="t1">Ticket</div><div class="t2">Parlay <span class="cnt">0</span></div></section>

  <section class="abs side" style="top:1081px">
    <div class="side-head" style="height:42px">My Bets</div>
    <div class="mybets-body">
      <div>↻ Refresh</div>
      <div class="nopend">No pending bets</div>
      <div class="viewall">View All</div>
    </div>
  </section>

  <!-- Live board -->
  <section class="abs board" style="top:213px">
    <div class="board-head">
      <span class="title"><svg width="18" height="18" viewBox="0 0 18 18"><circle cx="11" cy="3" r="2" fill="#fff"/><path d="M10 6l-4 3 3 2-2 6M10 6l2 5 4 1M6 9l-4 1" stroke="#fff" stroke-width="2" fill="none"/></svg>Today - Live</span>
      <span class="count">↻ 38</span>
      <span class="pick"><svg width="18" height="16" viewBox="0 0 16 14"><path d="M3 1h10v4a5 5 0 0 1-10 0z M1 2h2v3H2z M13 2h2l-1 3h-1z M7 10h2v2h2v2H5v-2h2z" fill="#fff"/></svg>Select League</span>
    </div>
    <div class="cols colhead">
      <div class="cell h-time">Time</div><div class="cell h-event">Event</div>
      <div class="cell h-full">Full Time</div><div class="cell h-half">First Half</div>
      <div class="cell h-more">+ More</div>
      <div class="cell sub" style="grid-column:3">A 1x2</div><div class="cell sub" style="grid-column:4">HDP</div><div class="cell sub" style="grid-column:5">OU</div><div class="cell sub" style="grid-column:6">1X2</div>
      <div class="cell sub" style="grid-column:7">HDP</div><div class="cell sub" style="grid-column:8">OU</div><div class="cell sub" style="grid-column:9">1X2</div>
    </div>
    <div class="league live"><span class="st">★</span>Austral Premier League<span class="rf">↻</span></div>
    <div class="match one">
      <div class="c-time"><span class="chart"></span>16.30<i>Live</i></div>
      <div class="c-event"><span class="fav">☆</span>Harbour City Mariners<div class="away">Southbank Victory</div></div>
      <div></div>
      <div><span class="l1" style="right:4px">0.77</span><span class="l2 blue" style="left:4px">0-0.5</span><span class="l2 red" style="right:4px">-0.95</span></div>
      <div><span class="l1 blue" style="left:4px">6-6.5</span><span class="l1 red" style="right:4px">-0.85</span><span class="l2" style="right:4px">0.65</span></div>
      <div></div><div></div><div></div><div></div>
      <div class="c-more">⇕13</div>
    </div>
  </section>

  <!-- Non-live board -->
  <section class="abs board" style="top:379px">
    <div class="board-head">
      <span class="title"><svg width="18" height="18" viewBox="0 0 18 18"><circle cx="11" cy="3" r="2" fill="#fff"/><path d="M10 6l-4 3 3 2-2 6M10 6l2 5 4 1M6 9l-4 1" stroke="#fff" stroke-width="2" fill="none"/></svg>Today - Non-Live</span>
      <span class="count">↻ 38</span>
      <span class="pick"><svg width="18" height="16" viewBox="0 0 16 14"><path d="M3 1h10v4a5 5 0 0 1-10 0z M1 2h2v3H2z M13 2h2l-1 3h-1z M7 10h2v2h2v2H5v-2h2z" fill="#fff"/></svg>Select League</span>
    </div>
    <div class="cols colhead">
      <div class="cell h-time">Time</div><div class="cell h-event">Event</div>
      <div class="cell h-full">Full Time</div><div class="cell h-half">First Half</div>
      <div class="cell h-more">+ More</div>
      <div class="cell sub" style="grid-column:3">A 1x2</div><div class="cell sub" style="grid-column:4">HDP</div><div class="cell sub" style="grid-column:5">OU</div><div class="cell sub" style="grid-column:6">1X2</div>
      <div class="cell sub" style="grid-column:7">HDP</div><div class="cell sub" style="grid-column:8">OU</div><div class="cell sub" style="grid-column:9">1X2</div>
    </div>

    <div class="league pre"><span class="st">★</span>Austral Premier League<span class="rf">↻</span></div>
    <div class="match"><div class="c-time"><span class="chart"></span>16.30<i>Live</i></div><div class="c-event"><span class="fav">☆</span>Harbour City Mariners<div class="away">Southbank Victory</div>Draw</div><div></div><div><span class="l1" style="right:4px">0.77</span><span class="l2 blue" style="left:4px">0-0.5</span><span class="l2 red" style="right:4px">-0.95</span></div><div><span class="l1 blue" style="left:4px">6-6.5</span><span class="l1 ou-o" style="left:49px">o</span><span class="l2 ou-o" style="left:49px">u</span><span class="l1 red" style="right:4px">-0.85</span><span class="l2" style="right:4px">0.65</span></div><div></div><div></div><div></div><div></div><div class="c-more">⇕13</div></div>

    <div class="league pre"><span class="st">★</span>Austral Premier League<span class="rf">↻</span></div>
    <div class="match"><div class="c-time"><span class="chart"></span>16.30<i>Live</i></div><div class="c-event"><span class="fav">☆</span>Harbour City Mariners<div class="away">Southbank Victory</div>Draw</div><div></div><div><span class="l1" style="right:4px">0.77</span><span class="l2 blue" style="left:4px">0-0.5</span><span class="l2 red" style="right:4px">-0.95</span></div><div><span class="l1 blue" style="left:4px">6-6.5</span><span class="l1 ou-o" style="left:49px">o</span><span class="l2 ou-o" style="left:49px">u</span><span class="l1 red" style="right:4px">-0.85</span><span class="l2" style="right:4px">0.65</span></div><div></div><div></div><div></div><div></div><div class="c-more">⇕13</div></div>
    <div class="match"><div class="c-time"><span class="chart"></span>16.30<i>Live</i></div><div class="c-event"><span class="fav">☆</span>Harbour City Mariners<div class="away">Southbank Victory</div>Draw</div><div></div><div><span class="l1" style="right:4px">0.77</span><span class="l2 blue" style="left:4px">0-0.5</span><span class="l2 red" style="right:4px">-0.95</span></div><div><span class="l1 blue" style="left:4px">6-6.5</span><span class="l1 ou-o" style="left:49px">o</span><span class="l2 ou-o" style="left:49px">u</span><span class="l1 red" style="right:4px">-0.85</span><span class="l2" style="right:4px">0.65</span></div><div></div><div></div><div></div><div></div><div class="c-more">⇕13</div></div>
    <div class="match"><div class="c-time"><span class="chart"></span>16.30<i>Live</i></div><div class="c-event"><span class="fav">☆</span>Harbour City Mariners<div class="away">Southbank Victory</div>Draw</div><div></div><div><span class="l1" style="right:4px">0.77</span><span class="l2 blue" style="left:4px">0-0.5</span><span class="l2 red" style="right:4px">-0.95</span></div><div><span class="l1 blue" style="left:4px">6-6.5</span><span class="l1 ou-o" style="left:49px">o</span><span class="l2 ou-o" style="left:49px">u</span><span class="l1 red" style="right:4px">-0.85</span><span class="l2" style="right:4px">0.65</span></div><div></div><div></div><div></div><div></div><div class="c-more">⇕13</div></div>

    <div class="league pre"><span class="st">★</span>Austral Premier League<span class="rf">↻</span></div>
    <div class="match"><div class="c-time"><span class="chart"></span>16.30<i>Live</i></div><div class="c-event"><span class="fav">☆</span>Harbour City Mariners<div class="away">Southbank Victory</div>Draw</div><div></div><div><span class="l1" style="right:4px">0.77</span><span class="l2 blue" style="left:4px">0-0.5</span><span class="l2 red" style="right:4px">-0.95</span></div><div><span class="l1 blue" style="left:4px">6-6.5</span><span class="l1 ou-o" style="left:49px">o</span><span class="l2 ou-o" style="left:49px">u</span><span class="l1 red" style="right:4px">-0.85</span><span class="l2" style="right:4px">0.65</span></div><div></div><div></div><div></div><div></div><div class="c-more">⇕13</div></div>

    <div class="league pre"><span class="st">★</span>Austral Premier League<span class="rf">↻</span></div>
    <div class="match"><div class="c-time"><span class="chart"></span>16.30<i>Live</i></div><div class="c-event"><span class="fav">☆</span>Harbour City Mariners<div class="away">Southbank Victory</div>Draw</div><div></div><div><span class="l1" style="right:4px">0.77</span><span class="l2 blue" style="left:4px">0-0.5</span><span class="l2 red" style="right:4px">-0.95</span></div><div><span class="l1 blue" style="left:4px">6-6.5</span><span class="l1 ou-o" style="left:49px">o</span><span class="l2 ou-o" style="left:49px">u</span><span class="l1 red" style="right:4px">-0.85</span><span class="l2" style="right:4px">0.65</span></div><div></div><div></div><div></div><div></div><div class="c-more">⇕13</div></div>
    <div class="match"><div class="c-time"><span class="chart"></span>16.30<i>Live</i></div><div class="c-event"><span class="fav">☆</span>Harbour City Mariners<div class="away">Southbank Victory</div>Draw</div><div></div><div><span class="l1" style="right:4px">0.77</span><span class="l2 blue" style="left:4px">0-0.5</span><span class="l2 red" style="right:4px">-0.95</span></div><div><span class="l1 blue" style="left:4px">6-6.5</span><span class="l1 ou-o" style="left:49px">o</span><span class="l2 ou-o" style="left:49px">u</span><span class="l1 red" style="right:4px">-0.85</span><span class="l2" style="right:4px">0.65</span></div><div></div><div></div><div></div><div></div><div class="c-more">⇕13</div></div>
    <div class="match"><div class="c-time"><span class="chart"></span>16.30<i>Live</i></div><div class="c-event"><span class="fav">☆</span>Harbour City Mariners<div class="away">Southbank Victory</div>Draw</div><div></div><div><span class="l1" style="right:4px">0.77</span><span class="l2 blue" style="left:4px">0-0.5</span><span class="l2 red" style="right:4px">-0.95</span></div><div><span class="l1 blue" style="left:4px">6-6.5</span><span class="l1 ou-o" style="left:49px">o</span><span class="l2 ou-o" style="left:49px">u</span><span class="l1 red" style="right:4px">-0.85</span><span class="l2" style="right:4px">0.65</span></div><div></div><div></div><div></div><div></div><div class="c-more">⇕13</div></div>
    <div class="match"><div class="c-time"><span class="chart"></span>16.30<i>Live</i></div><div class="c-event"><span class="fav">☆</span>Harbour City Mariners<div class="away">Southbank Victory</div>Draw</div><div></div><div><span class="l1" style="right:4px">0.77</span><span class="l2 blue" style="left:4px">0-0.5</span><span class="l2 red" style="right:4px">-0.95</span></div><div><span class="l1 blue" style="left:4px">6-6.5</span><span class="l1 ou-o" style="left:49px">o</span><span class="l2 ou-o" style="left:49px">u</span><span class="l1 red" style="right:4px">-0.85</span><span class="l2" style="right:4px">0.65</span></div><div></div><div></div><div></div><div></div><div class="c-more">⇕13</div></div>
    <div class="match"><div class="c-time"><span class="chart"></span>16.30<i>Live</i></div><div class="c-event"><span class="fav">☆</span>Harbour City Mariners<div class="away">Southbank Victory</div>Draw</div><div></div><div><span class="l1" style="right:4px">0.77</span><span class="l2 blue" style="left:4px">0-0.5</span><span class="l2 red" style="right:4px">-0.95</span></div><div><span class="l1 blue" style="left:4px">6-6.5</span><span class="l1 ou-o" style="left:49px">o</span><span class="l2 ou-o" style="left:49px">u</span><span class="l1 red" style="right:4px">-0.85</span><span class="l2" style="right:4px">0.65</span></div><div></div><div></div><div></div><div></div><div class="c-more">⇕13</div></div>
    <div class="match"><div class="c-time"><span class="chart"></span>16.30<i>Live</i></div><div class="c-event"><span class="fav">☆</span>Harbour City Mariners<div class="away">Southbank Victory</div>Draw</div><div></div><div><span class="l1" style="right:4px">0.77</span><span class="l2 blue" style="left:4px">0-0.5</span><span class="l2 red" style="right:4px">-0.95</span></div><div><span class="l1 blue" style="left:4px">6-6.5</span><span class="l1 ou-o" style="left:49px">o</span><span class="l2 ou-o" style="left:49px">u</span><span class="l1 red" style="right:4px">-0.85</span><span class="l2" style="right:4px">0.65</span></div><div></div><div></div><div></div><div></div><div class="c-more">⇕13</div></div>
    <div class="match"><div class="c-time"><span class="chart"></span>16.30<i>Live</i></div><div class="c-event"><span class="fav">☆</span>Harbour City Mariners<div class="away">Southbank Victory</div>Draw</div><div></div><div><span class="l1" style="right:4px">0.77</span><span class="l2 blue" style="left:4px">0-0.5</span><span class="l2 red" style="right:4px">-0.95</span></div><div><span class="l1 blue" style="left:4px">6-6.5</span><span class="l1 ou-o" style="left:49px">o</span><span class="l2 ou-o" style="left:49px">u</span><span class="l1 red" style="right:4px">-0.85</span><span class="l2" style="right:4px">0.65</span></div><div></div><div></div><div></div><div></div><div class="c-more">⇕13</div></div>
  </section>

  <footer class="abs foot">
    <span>Betting Rules</span><span>Contact Us</span><span>Privacy Policy</span><span>Responsible Gamnling</span><span>Terms &amp; Conditions</span><span>Tutorials</span>
  </footer>

</div>
</div>
</body>
</html>
```